Face cream packaging | Cosmetic start-up

This project is about creating design proposals for two different types of packaging. Once to a cream jar made of glass and once to a jar made of plastic.
Three different designs must be created for each type of jar. Later, the different packaging will be used as customization options in an online store for cosmetics.

- The packaging variant made of glass should have color gradients. Three different shades are to be chosen. (Preferably with the primary colors red, blue and green). Note: The designer can create other proposals at will if he has better ideas. The logo must be included in some form. (Link to manufacturer description: https://catalogue.vorelplast.example/en/portals/vorelplast/assets/40913526/tova-50-ml/)

- With the plastic type of packaging, the designer has a lot of freedom to design. The only requirement is that the design must be artistic. It doesn't matter whether abstract patterns, geometric figures, mandalas or just a basic color is chosen. The main thing is that the packaging inspires. The logo must be included in some form. (Link to manufacturer description: https://catalogue.vorelplast.example/en/portals/vorelplast/assets/40913519/rula-50-ml/)

Thank you in advance for your work and best regards
Ives

Target Market(s)

Young people with an affinity for social media and the web. Focus is on the female clientele.

Industry/Entity Type

Cosmetics

Font styles to use
Script

Colors
eea4c8
f59195
85cae6
cadf82

Requirements
Must have
• The logo must be included in some form. (PNG-File attached)
Nice to have
• Other types of packaging (can shape, packaging material)

```html
<!DOCTYPE html>
<html lang="en">
<head>
<meta charset="utf-8">
<title>Facial Cream Labels</title>
<link rel="stylesheet" href="https://fonts.googleapis.com/css2?family=Dawning+of+a+New+Day&family=Josefin+Sans:wght@300;400&display=swap">
<style>
  :root {
    --page: #ffffff;
    --ink: #ffffff;
    --violet-top: #9a45d8;
    --violet-mid: #f04f7c;
    --violet-low: #ee4d4e;
    --ocean-top: #58b6c2;
    --ocean-mid: #304a92;
    --ocean-low: #272a78;
    --forest-top: #5f9d5f;
    --forest-mid: #2e4a2f;
    --forest-low: #1d2a1f;
  }
  * { margin: 0; padding: 0; box-sizing: border-box; }
  html, body {
    width: 1200px; height: 654px; overflow: hidden;
    background: var(--page);
  }
  .range { position: relative; width: 1200px; height: 654px; }
  .label {
    position: absolute; top: 300px;
    width: 260px; height: 131px;
    font-family: "Josefin Sans", sans-serif;
    color: var(--ink);
  }
  .label--violet { left: 119px; background: linear-gradient(180deg, var(--violet-top) 0%, var(--violet-mid) 62%, var(--violet-low) 100%); }
  .label--ocean  { left: 481px; background: linear-gradient(180deg, var(--ocean-top) 0%, var(--ocean-mid) 55%, var(--ocean-low) 100%); }
  .label--forest { left: 839px; background: linear-gradient(180deg, var(--forest-top) 0%, var(--forest-mid) 55%, var(--forest-low) 100%); }
  .label__drip {
    position: absolute; left: 127px; top: 0;
    width: 7px; height: 103px;
    background: var(--page);
  }
  .label__product {
    position: absolute; left: 50px; top: 43px; width: 74px;
    font-size: 7.5px; font-weight: 400; letter-spacing: 5px;
    line-height: 10px; text-align: center; text-transform: uppercase;
    padding-left: 5px;
  }
  .label__brand {
    position: absolute; left: 142px; top: 36px;
    font-family: "Dawning of a New Day", cursive;
    font-size: 24px; font-weight: 400; line-height: 1;
    white-space: nowrap;
  }
  .label__volume {
    position: absolute; left: 0; width: 262px; top: 111px;
    text-align: center; font-size: 10.5px; font-weight: 300; letter-spacing: 0.6px;
  }
</style>
</head>
<body>
<main class="range">

  <section class="label label--violet">
    <div class="label__drip" role="img" aria-label="White cream drip ornament running down the label centre"></div>
    <p class="label__product">Facial Cream</p>
    <p class="label__brand">mira skin</p>
    <p class="label__volume">100ml &#8494;</p>
  </section>

  <section class="label label--ocean">
    <div class="label__drip" role="img" aria-label="White cream drip ornament running down the label centre"></div>
    <p class="label__product">Facial Cream</p>
    <p class="label__brand">mira skin</p>
    <p class="label__volume">100ml &#8494;</p>
  </section>

  <section class="label label--forest">
    <div class="label__drip" role="img" aria-label="White cream drip ornament running down the label centre"></div>
    <p class="label__product">Facial Cream</p>
    <p class="label__brand">mira skin</p>
    <p class="label__volume">100ml &#8494;</p>
  </section>

</main>
</body>
</html>
```